Web Design for Employee Benefits / Corporate Insurance Solutions Firm - Using Divi (by Vantor Pi...

*Please use Divi from vantor pixels to create the design.

Company Name: Harbourline Mira Group(Logo attached)

Colour scheme: White / Teal / Aquamarine / Grey

We are a firm that provides the following solutions for businesses:
- employee medical benefits
- office insurance
- talent retention / long-service retirement solutions
- keyman insurance

We need a website to provide information about our services, as well as password portals for employees of each company that we take care of.

Portals would provide specific information for employees of each company:
- employee handbook
- plan benefits & references
- claim forms

The site would also list articles for Human Resource Professionals and give them information about latest updates in the employee benefits / corporate culture best practices.

Target Market(s)

Human Resource Executives, Managing Directors, Chief Finance Officers, Employees

Industry/Entity Type

Business Consultant

Requirements
Must have
• Should be able to adjust the website widths & font sizes to be viewed on:
• - computer;
• - ipad;
• - smartphone

```html
<!DOCTYPE html>
<html lang="en">
<head>
<meta charset="utf-8">
<title>Harbourline Mira Group – Home</title>
<link href="https://fonts.googleapis.com/css2?family=Bebas+Neue&family=Roboto:wght@300;400;500&display=swap" rel="stylesheet">
<style>
  :root {
    --page-bg: #ffffff;
    --nav-bg: #2b3038;
    --nav-text: #ffffff;
    --accent: #3fe0b0;
    --aqua: #80f9d4;
    --teal: #008080;
    --teal-text: #0a8f86;
    --ink: #2c2c2c;
    --body-text: #444444;
    --copyright-bg: #3d3d3d;
    --hero-light: #eef0f2;
    --hero-mid: #b9bec4;
    --hero-dark: #3a3f48;
  }
  * { margin: 0; padding: 0; box-sizing: border-box; }
  html, body { width: 1200px; height: 1200px; overflow: hidden; background: var(--page-bg); }
  body { position: relative; font-family: "Roboto", Arial, sans-serif; color: var(--body-text); }

  .site { position: absolute; left: 282px; top: 140px; width: 636px; height: 918px; background: var(--page-bg); }

  .main-nav { position: absolute; left: 0; top: 0; width: 636px; height: 21px; background: var(--nav-bg); }
  .main-nav a { position: absolute; top: 6px; font-size: 7px; color: var(--nav-text); text-decoration: none; transform: translateX(-50%); white-space: nowrap; letter-spacing: 0.1px; }
  .main-nav a.is-active { color: var(--accent); }
  .main-nav a.is-active::after { content: ""; position: absolute; left: -2px; right: -2px; top: 14px; height: 2px; background: var(--accent); }

  .hero { position: absolute; left: 0; top: 21px; width: 636px; height: 274px;
    background:
      radial-gradient(ellipse at 15% 55%, rgba(40,45,60,0.75) 0 18%, transparent 40%),
      radial-gradient(ellipse at 82% 72%, rgba(60,45,40,0.7) 0 14%, transparent 34%),
      radial-gradient(ellipse at 35% 8%, rgba(90,95,105,0.6) 0 16%, transparent 34%),
      linear-gradient(135deg, var(--hero-light), #ffffff 55%, var(--hero-mid)); }
  .hero-brand { position: absolute; left: 186px; top: 49px; width: 264px; height: 160px; background: rgba(255,255,255,0.78);
    display: flex; flex-direction: column; align-items: center; justify-content: center; gap: 6px; }
  .hero-brand-mark { width: 60px; height: 60px; border-radius: 50%; background: var(--teal); }
  .hero-brand-name { font-family: "Roboto", Arial, sans-serif; font-weight: 300; font-size: 19px; letter-spacing: 2.5px; color: var(--ink); text-transform: uppercase; text-align: center; line-height: 1.2; }

  .welcome { position: absolute; left: 0; top: 295px; width: 636px; height: 281px; }
  .welcome svg { position: absolute; left: 0; top: 0; }
  .section-title { font-family: "Bebas Neue", Impact, sans-serif; font-size: 30px; line-height: 1; color: var(--ink); letter-spacing: 0.3px; }
  .welcome .section-title { position: absolute; left: 75px; top: 25px; }
  .title-rule { position: absolute; left: 79px; top: 54px; width: 46px; height: 1px; background: var(--teal); }
  .welcome-intro { position: absolute; left: 75px; top: 63px; width: 222px; font-size: 6.8px; line-height: 11.4px; text-align: justify; color: var(--body-text); }
  .solutions-lead { position: absolute; left: 75px; top: 105px; font-size: 6.8px; color: var(--body-text); }
  .solutions-list { position: absolute; left: 75px; top: 116px; list-style: none; font-size: 6.8px; line-height: 11.3px; color: var(--body-text); }
  .solutions-list li { position: relative; padding-left: 14px; height: 11.3px; }
  .solutions-list li.has-bullet::before { content: ""; position: absolute; left: 3px; top: 4px; width: 3.5px; height: 3.5px; background: var(--teal); }

  .services { position: absolute; left: 75px; top: 533px; width: 520px; }
  .services .section-title { margin-bottom: 13px; }
  .service-item { font-size: 6.6px; line-height: 11.3px; color: var(--body-text); margin-bottom: 11.3px; white-space: nowrap; }
  .service-name { color: var(--teal-text); font-weight: 500; }

  .contact-band { position: absolute; left: 0; top: 861px; width: 636px; height: 37px; background: var(--teal); color: #ffffff; }
  .contact-item { position: absolute; top: 0; height: 37px; display: flex; align-items: center; gap: 6px; font-size: 13px; font-weight: 300; white-space: nowrap; }
  .contact-phone { left: 72px; }
  .contact-email { left: 282px; }
  .contact-at { font-size: 30px; font-weight: 400; line-height: 1; margin-top: -4px; }
  .copyright { position: absolute; left: 0; top: 898px; width: 636px; height: 20px; background: var(--copyright-bg); color: #e6e6e6; font-size: 5.6px; text-align: center; line-height: 20px; }
</style>
</head>
<body>
  <div class="site">
    <nav class="main-nav">
      <a class="is-active" href="#" style="left:163px">HOME</a>
      <a href="#" style="left:221px">ABOUT US</a>
      <a href="#" style="left:288px">SERVICES</a>
      <a href="#" style="left:347px">LATEST NEWS</a>
      <a href="#" style="left:402px">PLANS</a>
      <a href="#" style="left:464px">CONTACT US</a>
    </nav>

    <header class="hero" role="img" aria-label="Overhead photo of business people meeting around a white table with laptops and documents">
      <div class="hero-brand">
        <div class="hero-brand-mark"></div>
        <div class="hero-brand-name">Harbourline<br>Mira Group</div>
      </div>
    </header>

    <section class="welcome">
      <svg width="636" height="281" viewBox="0 0 636 281" aria-hidden="false">
        <defs>
          <linearGradient id="handshakeTone" x1="0" y1="0" x2="1" y2="0">
            <stop offset="0" stop-color="#80f9d4" stop-opacity="0"/>
            <stop offset="0.3" stop-color="#5fc8b0"/>
            <stop offset="0.65" stop-color="#3b4a52"/>
            <stop offset="1" stop-color="#2c3338"/>
          </linearGradient>
          <clipPath id="welcomeShape">
            <polygon points="0,0 636,0 636,281 0,167"/>
          </clipPath>
        </defs>
        <polygon points="0,0 636,0 636,281 0,167" fill="#80f9d4"/>
        <g clip-path="url(#welcomeShape)">
          <rect x="300" y="0" width="336" height="281" fill="url(#handshakeTone)" role="img" aria-label="Photo of two businessmen shaking hands"/>
        </g>
      </svg>
      <h2 class="section-title">Welcome</h2>
      <div class="title-rule"></div>
      <p class="welcome-intro">Lorem ipsum dolor sit amet, consectetur adipiscing elit. Proin consequat tempus finibus. Cras congue nibh nec leo ultrices, venenatis lacinia augue laoreet.</p>
      <p class="solutions-lead">We are a firm that provides the following solutions for businesses:</p>
      <ul class="solutions-list">
        <li>Employee medical benefits</li>
        <li class="has-bullet">Office insurance</li>
        <li class="has-bullet">Talent retention / long-service retirement solutions</li>
        <li class="has-bullet">Keyman insurance</li>
        <li class="has-bullet"></li>
      </ul>
    </section>

    <section class="services">
      <h2 class="section-title">Services</h2>
      <p class="service-item">1. <span class="service-name">Review</span> (Existing Clients Only)<br>
        Would you want to know the utilization experience of your company's employee benefits?<br>
        Do you need information to help with the forward budgeting for your next work year?<br>
        Do you have concerns or issues to highlight so as to improve the experience of the existing employee benefits program?<br>
        Let us know and we will be pleased to be on-site to have a discussion with your HR Executives &amp; Administrators.</p>
      <p class="service-item">2. <span class="service-name">Consultation</span> (for existing clients only)<br>
        Do you need help with the claim process or claim outcome?<br>
        Do you need advice or assistance with your personal portfolio?<br>
        Gather a few of your colleagues who may request time for a private conversation with us, and we'll be happy to assist on-site.</p>
      <p class="service-item">3. <span class="service-name">Draft A New Solution</span><br>
        Are you a new start-up seeking to retain your talent pool with medical benefits?<br>
        Is your current program too outdated and you want a fresh new approach to employee benefits?<br>
        Let's work together to create new solutions to meet the current needs of your employees.</p>
      <p class="service-item">4. <span class="service-name">Review &amp; Assess</span><br>
        Would you like an unbiased opinion of your current employee benefits program?<br>
        Do you have a need to review and make improvements on your current employee benefits program?<br>
        Get in touch with us for an initial meeting for this review.</p>
      <p class="service-item">5. <span class="service-name">Speaking Engagement</span> (Learning Day)<br>
        Would you like your staff to be more competent with their personal finances?<br>
        How do we enable each employee to utilise the National framework of health insurance?<br>
        If you would like us to speak and share to your employees, feel free to contact us for a discussion that may meet your needs.</p>
    </section>

    <footer>
      <div class="contact-band">
        <div class="contact-item contact-phone">
          <svg width="32" height="32" viewBox="0 0 32 32" aria-hidden="true">
            <circle cx="16" cy="16" r="14.5" fill="none" stroke="#ffffff" stroke-width="2"/>
            <path d="M11.5 8.5c1-.6 2-.3 2.5.6l1.3 2.6c.4.8.2 1.6-.5 2.1l-1 .7c.6 2 2 3.9 3.8 5l1-.8c.7-.5 1.6-.5 2.2.2l1.8 2.1c.6.7.5 1.7-.3 2.3l-1.2.9c-1.3 1-3.3.6-5.2-.8-3-2.2-5.1-5.6-5.7-8.9-.3-2 .1-3.4 1.3-4z" fill="#ffffff"/>
          </svg>
          <span>CALL US: +0011 48207</span>
        </div>
        <div class="contact-item contact-email">
          <span class="contact-at">@</span>
          <span>eMAIL US: info@harbourlinemira.com</span>
        </div>
      </div>
      <div class="copyright">Copyright2018. Harbourline Mira Group. All rights reserved</div>
    </footer>
  </div>
</body>
</html>
```